Australian Web Design company needs a business card design

We need a business card design for a Sydney based Web Design/Development company called "Tall Pine Web Design". We design, build and deploy websites for small to medium sized businesses. The final design should be clean and communicate that we are a professional and supportive company.
I'd like the Icon to be abstract. Something that embodies the power of the internet, needs to be clean/professional and show that we are human and that we support our customers. Hope that helps.
Target Market(s)
All small to medium businesses
Industry/Entity Type
Business
Contact Information for Business Card
Martin Forbes
Tall Pine Web Design
17 Wattle Grove Road
West Kelsworth
NSW 2250
0438 527 064
martin@tallpinewebdesign.com.au
www.tallpinewebdesign.com.au

```html
<!DOCTYPE html>
<html lang="en">
<head>
<meta charset="utf-8">
<title>Business Card Design – Tall Pine Web Design</title>
<link rel="stylesheet" href="https://fonts.googleapis.com/css2?family=Source+Sans+3:wght@400;600;700&family=Montserrat:wght@700&display=swap">
<style>
  :root {
    --board: #ffffff;
    --ink: #231f20;
    --paper: #b9c3c8;
    --slate: #2b343c;
    --red: #c00000;
    --red-deep: #8a0000;
    --white: #ffffff;
  }
  * { margin: 0; padding: 0; box-sizing: border-box; }
  html, body { width: 1200px; height: 1200px; overflow: hidden; background: var(--board); }
  .board {
    position: relative; width: 1240px; height: 1240px;
    transform: scale(0.9677); transform-origin: 0 0;
    font-family: "Source Sans 3", "Myriad Pro", sans-serif; color: var(--ink);
  }
  .project-info { position: absolute; left: 729px; top: 68px; font-size: 26px; line-height: 34px; }
  .palette-title { position: absolute; left: 731px; top: 203px; font-size: 25px; }
  .swatch { position: absolute; top: 250px; width: 86px; height: 86px; border-radius: 20px; }
  .swatch--slate { left: 729px; background: var(--slate); }
  .swatch--red { left: 844px; background: radial-gradient(circle at 50% 45%, var(--red) 0%, var(--red-deep) 100%); }
  .swatch-label { position: absolute; top: 350px; font-size: 16px; }
  .swatch-label--slate { left: 731px; }
  .swatch-label--red { left: 846px; }
  .card {
    position: absolute; top: 420px; width: 329px; height: 508px;
    filter: drop-shadow(9px 9px 7px rgba(0,0,0,0.45));
  }
  .card--front { left: 187px; }
  .card--back { left: 622px; }
  .card svg { position: absolute; inset: 0; display: block; }
  .brand-name {
    position: absolute; left: 22px; top: 156px;
    font-family: "Montserrat", sans-serif; font-weight: 700; font-size: 30px;
    line-height: 40px; color: var(--white);
  }
  .brand-name span { display: block; }
  .brand-name span + span { padding-left: 60px; }
  .front-url { position: absolute; right: 17px; bottom: 38px; font-size: 13px; }
  .holder { position: absolute; left: 32px; top: 172px; color: var(--white); }
  .holder-name { font-weight: 700; font-size: 29px; line-height: 34px; letter-spacing: 0.5px; }
  .holder-company { font-size: 23px; line-height: 30px; }
  .contact-list { position: absolute; left: 32px; top: 344px; list-style: none; font-size: 15px; line-height: 20px; }
  .contact-list li { display: flex; align-items: flex-start; margin-bottom: 10px; }
  .contact-list svg { position: static; flex: none; width: 14px; height: 14px; margin: 3px 4px 0 0; fill: var(--red); }
  .description { position: absolute; left: 195px; top: 1018px; font-size: 26px; line-height: 34px; }
</style>
</head>
<body>
<main class="board">
  <div class="project-info">
    <p>Project name: Business Card Design</p>
    <p>Client: Tall Pine Web Design</p>
    <p>Style: Clean and personable</p>
  </div>

  <p class="palette-title">CMYK (%)</p>
  <div class="swatch swatch--slate"></div>
  <div class="swatch swatch--red"></div>
  <p class="swatch-label swatch-label--slate">68,56,49,53</p>
  <p class="swatch-label swatch-label--red">0,100,100,0</p>

  <section class="card card--front">
    <svg viewBox="0 0 329 508" width="329" height="508" aria-hidden="true">
      <defs>
        <radialGradient id="frontRed" cx="0.6" cy="0.35" r="0.7">
          <stop offset="0" stop-color="#c40000"/>
          <stop offset="1" stop-color="#860000"/>
        </radialGradient>
      </defs>
      <rect width="329" height="508" fill="var(--paper)"/>
      <polygon points="0,0 329,163 0,230" fill="url(#frontRed)"/>
      <polygon points="0,230 329,163 329,385" fill="var(--slate)"/>
    </svg>
    <p class="brand-name"><span>Tall Pine</span><span>Web Design</span></p>
    <p class="front-url">www.tallpinewebdesign.com.au</p>
  </section>

  <section class="card card--back">
    <svg viewBox="0 0 329 508" width="329" height="508" aria-hidden="true">
      <defs>
        <radialGradient id="backRed" cx="0.55" cy="0.5" r="0.7">
          <stop offset="0" stop-color="#c40000"/>
          <stop offset="1" stop-color="#860000"/>
        </radialGradient>
      </defs>
      <rect width="329" height="508" fill="var(--paper)"/>
      <polygon points="78,54 329,2 329,228" fill="var(--slate)"/>
      <polygon points="0,0 329,228 0,318" fill="url(#backRed)"/>
    </svg>
    <div class="holder">
      <p class="holder-name">Martin Forbes</p>
      <p class="holder-company">Tall Pine Web Design</p>
    </div>
    <ul class="contact-list">
      <li>
        <svg viewBox="0 0 14 14"><path d="M7 1 L13 7 H11 V13 H8.5 V9 H5.5 V13 H3 V7 H1 Z"/></svg>
        <span>17 Wattle Grove Road West Kelsworth<br>NSW 2250</span>
      </li>
      <li>
        <svg viewBox="0 0 14 14"><path d="M8 1 L12 3 L7 13 L3 11 Z M8.4 2.6 L5 9.6 L6.4 10.3 L9.8 3.3 Z"/></svg>
        <span>0438 527 064</span>
      </li>
      <li>
        <svg viewBox="0 0 14 14"><path d="M7 1a6 6 0 1 0 3.5 10.9l-.8-1.2A4.6 4.6 0 1 1 11.6 7v.8c0 .8-.5 1.2-1 1.2s-1-.4-1-1.2V4.5H8.3v.5A2.8 2.8 0 1 0 8.6 9.3 2.2 2.2 0 0 0 10.6 10.4 2.4 2.4 0 0 0 13 7.8V7A6 6 0 0 0 7 1Zm0 7.5a1.5 1.5 0 1 1 0-3 1.5 1.5 0 0 1 0 3Z"/></svg>
        <span>martin@tallpinewebdesign.com.au</span>
      </li>
      <li>
        <svg viewBox="0 0 14 14"><path d="M7 1a6 6 0 1 0 0 12A6 6 0 0 0 7 1Zm-1 1.3V4H3.2A4.8 4.8 0 0 1 6 2.3ZM2.6 5H6v1.5H2.3A4.8 4.8 0 0 1 2.6 5Zm-.3 2.5H6V9H2.6a4.8 4.8 0 0 1-.3-1.5ZM3.2 10H6v1.7A4.8 4.8 0 0 1 3.2 10ZM8 11.7V10h2.8A4.8 4.8 0 0 1 8 11.7ZM11.4 9H8V7.5h3.7a4.8 4.8 0 0 1-.3 1.5ZM8 6.5V5h3.4a4.8 4.8 0 0 1 .3 1.5ZM8 4V2.3A4.8 4.8 0 0 1 10.8 4Z"/></svg>
        <span>www.tallpinewebdesign.com.au</span>
      </li>
    </ul>
  </section>

  <div class="description">
    <p>Description</p>
    <p>Create a double-sided business card for a Web Design/Development company.</p>
    <p>The design is eyes-catching with geometrical elements which make design dynamic.</p>
    <p>The paper made of eco-friendly recycling material and has craft facture.</p>
    <p>The main design colors are grey, metallic red and dark grey.</p>
  </div>
</main>
</body>
</html>
```